Accountancy practice needs a wordpress website redesign for growth

We are a growing accountancy practice - headcount and revenues have doubled in the last 2 years. We are continuing to grow. We only had a website made around 12 months ago but the company we used offered very little in terms of creativity and ideas of how to make it look modern and eye-catching. We want to redesign the website to make it look premium and professional because we are starting to launch more marketing and drive more traffic to the site.

The current website is www.tovelbrookaccountants.co.uk. The website was built in wordpress.

The logo has been uploaded. The main 2 colour hex codes are: 0E74BC and 14A79D.

We are open to changing the fonts in the website and welcome suggestions for this too.

Following on from this we will launch a project to design brochures and one-page flyers that we can fill with useful information about what we do and also create lead-generators to download from the website. So the design of the website will influence the overall brand and feel of all of the marketing collateral.

Target Market(s)

Property businesses and entrepreneurial, growth mindset clients

Industry/Entity Type

Accountancy

Number of Pages Required

3 page

Font styles to use
Sans Serif

Colors

Designer to choose colors to be used in the design.

Requirements
Must have
• A modern and professional feel. 3 fonts - most websites seem to use 3 different fonts now and I like this. We have our green and blue colours but I do not want too much of this all over the site, stick to blacks, whites and greys with the blue and green used for emphasis and accents.
Nice to have
• The coloured spaces should have some "depth" to them, eg a small pattern in the white spaces so its not just a solid whie background.

```html
<!DOCTYPE html>
<html lang="en">
<head>
<meta charset="utf-8">
<title>Tovelbrook Accountants</title>
<link href="https://fonts.googleapis.com/css2?family=Montserrat:wght@600;700;800&family=Poppins:ital,wght@0,400;0,500;0,600;1,400&family=Lato:wght@400;700&display=swap" rel="stylesheet">
<style>
:root{
  --blue:#0E74BC;
  --teal:#14A79D;
  --ink:#1d1d1f;
  --grey:#5b5f66;
  --line:#e3e6ea;
  --pale:#f2f4f6;
  --white:#fff;
}
*{box-sizing:border-box;margin:0;padding:0}
html,body{width:1200px;height:4754px;overflow:hidden}
body{position:relative;font-family:"Poppins",sans-serif;color:var(--ink);background:var(--white)}
.abs{position:absolute}
h1,h2,h3{font-family:"Montserrat",sans-serif}
.btn{position:absolute;display:flex;align-items:center;justify-content:center;font:500 10px "Poppins",sans-serif;letter-spacing:.5px;text-transform:uppercase;border:2px solid var(--teal);border-bottom-width:5px;color:var(--teal);background:#fff}
.logo{position:absolute;display:flex;align-items:center;gap:10px;font:700 18px/1 "Montserrat",sans-serif;letter-spacing:1px;color:var(--blue)}
.logo i{width:22px;height:22px;background:var(--teal);display:block}
.logo span{display:block}

/* header */
.topbar{left:730px;top:0;width:470px;height:30px;background:var(--teal);color:#fff;font:600 10px "Poppins",sans-serif;display:flex;align-items:center;gap:16px;padding-left:46px;clip-path:polygon(0 0,100% 0,100% 100%,24px 100%)}
.nav{left:460px;top:50px;display:flex;gap:22px;font:500 10px "Poppins",sans-serif;text-transform:uppercase;color:var(--ink)}
.nav .on{color:var(--teal);border-top:2px solid var(--teal);padding-top:2px;margin-top:-4px}
.get{left:955px;top:43px;width:97px;height:30px;background:var(--blue);color:#fff;font:600 10px "Poppins",sans-serif;display:flex;align-items:center;justify-content:center;text-transform:uppercase}

/* hero */
.hero{left:0;top:85px;width:1200px;height:565px;background:linear-gradient(160deg,#3bb7a9 0%,#1e93b4 50%,#0E74BC 100%)}
.hero h1{position:absolute;left:148px;top:136px;width:560px;white-space:nowrap;font-size:28px;line-height:41px;font-weight:800;color:#fff;text-transform:uppercase}
.hero p{position:absolute;left:148px;top:308px;width:460px;white-space:nowrap;font-size:19px;line-height:26px;color:#fff;font-weight:500}
.hero .btn{left:148px;top:388px;width:203px;height:33px;border:none;border-left:5px solid var(--teal);color:var(--blue)}
.hero-art{left:655px;top:90px;width:410px;height:270px;border-radius:12px;background:linear-gradient(135deg,rgba(255,255,255,.35),rgba(255,255,255,.12))}

/* stakes */
.stakes h2{position:absolute;left:148px;top:720px;font-size:26px;color:var(--teal)}
.stake{position:absolute;left:148px;width:905px;height:48px;display:flex;align-items:center;gap:12px;font-size:16px;color:var(--ink);border-bottom:1px solid var(--line)}

/* partner */
.partner{left:0;top:985px;width:1200px;height:950px;background:linear-gradient(180deg,#eef1f4,#f7f8fa 70%,#fff)}
.partner h2{position:absolute;left:0;top:68px;width:1200px;text-align:center;font-size:24px;line-height:34px;color:var(--teal)}
.card{position:absolute;left:218px;width:762px;height:113px;background:#fff;display:flex;box-shadow:0 2px 8px rgba(0,0,0,.06)}
.card .ic{width:128px;flex:none;border-right:2px solid var(--pale);display:flex;align-items:center;justify-content:center}
.card .tx{padding:30px 28px}
.card h3{font:500 16px "Poppins",sans-serif;color:var(--blue);margin-bottom:10px}
.card p{font-size:11.5px;line-height:15px;color:var(--grey)}
.partner .side{position:absolute;top:818px;width:1200px;text-align:center;font-size:13px}

/* about */
.about p{position:absolute;left:148px;width:450px;font-size:12px;line-height:18.5px;color:var(--grey)}
.about .hl{color:var(--teal);font-weight:600}
.about-photo{left:632px;top:2007px;width:420px;height:362px;background:linear-gradient(135deg,#c9d3dc,#7a8a99 60%,#3a4550);clip-path:polygon(20% 0,100% 0,100% 100%,0 100%)}
.about-frame{left:610px;top:2007px;width:442px;height:378px}

/* testimonials */
.testi{left:0;top:2455px;width:1200px;height:420px;background:linear-gradient(180deg,#14A79D 0%,#0f8db0 45%,#0E74BC 100%);color:#fff}
.testi h2{position:absolute;top:62px;width:1200px;text-align:center;font-size:24px}
.testi .q{position:absolute;left:220px;width:760px;text-align:center;font-style:italic;font-size:12.5px;line-height:20px}
.arrow{position:absolute;top:175px;width:34px;height:34px;border:2px solid #fff;display:flex;align-items:center;justify-content:center}
.person{left:530px;top:300px;width:58px;height:52px;background:linear-gradient(#dfe5ea,#9aa7b2)}
.who{left:612px;top:307px;font:600 12.5px "Montserrat",sans-serif;line-height:18px}
.who small{display:block;font:400 11px "Poppins",sans-serif}

/* plan */
.plan h2{position:absolute;top:2940px;width:1200px;text-align:center;font-size:24px;color:var(--teal)}
.step{position:absolute;top:3007px;width:280px;text-align:center}
.step .circ{position:relative;margin:0 auto;width:96px;height:96px;border:2px solid var(--blue);border-radius:50%;display:flex;align-items:center;justify-content:center}
.step .n{position:absolute;bottom:-11px;left:37px;width:22px;height:22px;border-radius:50%;background:var(--teal);color:#fff;font:600 11px/22px "Poppins",sans-serif}
.step h3{font:500 17px "Poppins",sans-serif;color:var(--teal);margin:26px 0 18px}
.step p{font-size:11.5px;line-height:17px;color:var(--grey)}

/* story */
.story-photo{left:148px;top:3478px;width:400px;height:425px;background:linear-gradient(135deg,#e8ecef,#aeb8c1 55%,#5c6974);clip-path:polygon(0 0,100% 0,60% 100%,0 100%)}
.story p{position:absolute;left:598px;width:455px;font-size:11.5px;line-height:18px;color:var(--grey)}
.story .hl{color:var(--blue);font-weight:500}

/* video band */
.band-bg{left:0;top:4155px;width:1200px;height:599px;background:linear-gradient(180deg,#14A79D,#1290b0 50%,#0E74BC)}
.video{left:148px;top:3997px;width:904px;height:370px;background:linear-gradient(120deg,#8d969e,#d7dde2 55%,#eef1f3)}
.play{left:580px;top:4100px}

/* footer */
.footer{color:#fff}
.footer h4{position:absolute;font:500 15px "Poppins",sans-serif}
.footer ul{position:absolute;list-style:none;font:400 11px/21px "Lato",sans-serif}
.contact{position:absolute;left:408px;display:flex;gap:12px;font-size:11px;line-height:14px}
.social{position:absolute;top:4565px;width:32px;height:32px;border-radius:50%;background:#fff}
.badge{position:absolute;top:4560px;height:48px;background:#fff;border-radius:6px}
.rule{left:148px;top:4690px;width:904px;height:1px;background:rgba(255,255,255,.4)}
.copy{left:0;top:4706px;width:1200px;text-align:center;font-size:10px;color:#fff}
</style>
</head>
<body>

<!-- header -->
<div class="logo" style="left:148px;top:24px"><i></i><span>TOVELBROOK<br>ACCOUNTANTS</span></div>
<div class="abs topbar"><span>CLIENT PORTAL LOGIN</span><span>|</span><span>BOOK A DISCOVERY CALL</span></div>
<nav class="abs nav"><span class="on">Home</span><span>About us ⌄</span><span>Who we help ⌄</span><span>Thoughts</span><span>Switching accountants</span></nav>
<div class="abs get">Get in touch</div>

<!-- hero -->
<section class="abs hero">
  <h1>Expert accountancy<br>services for property<br>investors and ambitious<br>business owners</h1>
  <p>Earn more, keep more, run your business<br>with confidence</p>
  <div class="btn">Book a discovery call now</div>
  <div class="abs hero-art" role="img" aria-label="Illustration of an accountant beside a large calculator, coins and banknotes"></div>
</section>

<!-- stakes -->
<section class="stakes">
  <h2>THE STAKES</h2>
  <div>
    <div class="stake" style="top:768px"><svg width="16" height="16" viewBox="0 0 16 16"><path d="M2 8h11M9 4l4 4-4 4" stroke="#14A79D" stroke-width="2.4" fill="none"/></svg>Does your accountant understand property tax?</div>
    <div class="stake" style="top:824px"><svg width="16" height="16" viewBox="0 0 16 16"><path d="M2 8h11M9 4l4 4-4 4" stroke="#0E74BC" stroke-width="2.4" fill="none"/></svg>Are you tired of not getting the support you need from your accountant to run your business?</div>
    <div class="stake" style="top:880px;border:none"><svg width="16" height="16" viewBox="0 0 16 16"><path d="M2 8h11M9 4l4 4-4 4" stroke="#14A79D" stroke-width="2.4" fill="none"/></svg>How much is unclear advice and poor accounting services costing you and your business?</div>
  </div>
</section>

<!-- partner -->
<section class="abs partner">
  <h2>YOU NEED AN ACCOUNTANT THAT ACTS AS A<br>BUSINESS PARTNER</h2>
  <div class="card" style="top:154px"><div class="ic"><svg width="56" height="56" viewBox="0 0 56 56" fill="none" stroke="#0E74BC" stroke-width="2"><circle cx="22" cy="16" r="9"/><path d="M6 50c0-10 7-17 16-17s16 7 16 17"/><path d="M36 38l8-7 8 7v10H36z" stroke="#14A79D"/></svg></div><div class="tx"><h3>Experts at Property</h3><p>We help you through your property journey, giving expert tax advice at every step</p></div></div>
  <div class="card" style="top:281px"><div class="ic"><svg width="56" height="56" viewBox="0 0 56 56" fill="none" stroke="#0E74BC" stroke-width="2"><circle cx="16" cy="10" r="6"/><path d="M10 50V22h12v28"/><circle cx="38" cy="26" r="8" stroke="#14A79D"/><path d="M35 36h6v5h-6z" stroke="#14A79D"/></svg></div><div class="tx"><h3>Entrepreneurial Accountants</h3><p>Get a business partner that understands what it takes to run and grow a business</p></div></div>
  <div class="card" style="top:409px"><div class="ic"><svg width="56" height="56" viewBox="0 0 56 56" fill="none" stroke="#0E74BC" stroke-width="2"><circle cx="28" cy="22" r="11"/><path d="M31 17h-5a2.5 2.5 0 000 5h4a2.5 2.5 0 010 5h-5M28 14v16" stroke="#14A79D"/><path d="M6 44c8-4 16 4 24 0l18-6"/></svg></div><div class="tx"><h3>Finance function</h3><p>We can run your entire finance function, taking away the hassle of managing the finances</p></div></div>
  <div class="card" style="top:536px"><div class="ic"><svg width="56" height="56" viewBox="0 0 56 56" fill="none" stroke="#0E74BC" stroke-width="2"><path d="M14 28a14 14 0 0128 0"/><rect x="10" y="26" width="7" height="12" rx="3"/><rect x="39" y="26" width="7" height="12" rx="3"/><path d="M42 38c0 8-6 10-12 10" stroke="#14A79D"/></svg></div><div class="tx"><h3>Know who to contact</h3><p>You will have a client delivery team – no more confusion about who to contact</p></div></div>
  <div class="card" style="top:665px"><div class="ic"><svg width="56" height="56" viewBox="0 0 56 56" fill="none" stroke="#0E74BC" stroke-width="2"><path d="M4 24l10-6 10 4 8-4 10 2 10 6"/><path d="M14 34l8 8 4-2 4 4 4-2 4 2 8-10" stroke="#14A79D"/></svg></div><div class="tx"><h3>A business partner</h3><p>Never worry about the finances and taxes again. Make the move from worker to owner and keep more, work less and get your time back.</p></div></div>
  <p class="side">Get an accountant that is on your side.</p>
  <div class="btn" style="left:545px;top:845px;width:112px;height:35px">Book a call</div>
</section>

<!-- about -->
<section class="about">
  <p style="top:2066px">We understand that running a successful business requires an incredible amount of effort and dedication – we do it ourselves.</p>
  <p style="top:2121px">We understand that building a property business takes an unbelievable amount of time and commitment – we do it ourselves.</p>
  <p style="top:2176px">You want to know that the decisions you make are based on sound, correct advice and you want to be able to talk to someone you trust for that advice. So don't worry – we've got this.</p>
  <p style="top:2250px"><span class="hl">Make the 115 years visually stand out:</span><br>115 years + combined experience covering property tax through to completing business sales and purchases worth $1bn.</p>
  <svg class="abs about-frame" viewBox="0 0 442 378"><polygon points="98,0 120,0 22,378 0,378" fill="#0E74BC"/><rect x="22" y="366" width="420" height="12" fill="#0E74BC"/></svg>
  <div class="abs about-photo" role="img" aria-label="Photo of two business professionals reviewing documents at a desk"></div>
</section>

<!-- testimonials -->
<section class="abs testi">
  <h2>TESTIMONIALS</h2>
  <p class="q" style="top:112px">"In 2020 we were frustrated with our in-house FD and took to step of asking Tovelbrook Accountants (who we had worked with for 15 years) to step in and fulfil the role through their Virtual Finance Office service. It was a big decision to make, but one we are very happy that we did because of the impact it has had on our finances. Deadlines are never missed, audits are completed without issue and our banks have commented that they have never had more comfort with our numbers.</p>
  <p class="q" style="top:232px">They have helped us rebuild back end systems, cashflow models and worksheets and also now taken on our payroll. We are looking at more ways to work closely with Tovelbrook Accountants because of the value they can add."</p>
  <div class="arrow" style="left:148px"><svg width="14" height="10" viewBox="0 0 14 10"><path d="M13 5H2M5 1L1 5l4 4" stroke="#fff" stroke-width="1.5" fill="none"/></svg></div>
  <div class="arrow" style="left:1018px;background:#fff"><svg width="14" height="10" viewBox="0 0 14 10"><path d="M1 5h11M9 1l4 4-4 4" stroke="#0E74BC" stroke-width="1.5" fill="none"/></svg></div>
  <div class="abs person" role="img" aria-label="Portrait photo of the client"></div>
  <div class="abs who">RAVI KESSLER,<small>MD of Marlow Group</small></div>
</section>

<!-- plan -->
<section class="plan">
  <h2>PLAN</h2>
  <div class="step" style="left:150px"><div class="circ"><svg width="36" height="36" viewBox="0 0 36 36" fill="none" stroke="#0E74BC" stroke-width="2"><path d="M8 4l6 1 2 7-4 3a20 20 0 009 9l3-4 7 2 1 6c-14 2-28-12-24-24z"/><path d="M22 6a9 9 0 018 8M22 11a4 4 0 013 3"/></svg><span class="n">1</span></div><h3>Get in touch</h3><p>Book a call with us where we can get to know you better, understand your business, your challenges and where you want to get to in order to see if we're a good fit to work with you.</p></div>
  <div class="step" style="left:460px"><div class="circ"><svg width="32" height="36" viewBox="0 0 32 36" fill="none" stroke="#0E74BC" stroke-width="2"><rect x="3" y="5" width="26" height="29" rx="2"/><rect x="10" y="2" width="12" height="6"/><path d="M9 15h14M9 21h14M9 27h14"/></svg><span class="n">2</span></div><h3>Get a plan</h3><p>We'll put together a plan to help you to get your structure right, start to manage your finances better, find ways to pay less tax and take the stress of your accounts away.</p></div>
  <div class="step" style="left:770px"><div class="circ"><svg width="36" height="34" viewBox="0 0 36 34" fill="none" stroke="#0E74BC" stroke-width="2"><rect x="4" y="18" width="7" height="14"/><rect x="15" y="10" width="7" height="22"/><rect x="26" y="3" width="7" height="29"/></svg><span class="n">3</span></div><h3>Get going</h3><p>We take over everything from your old accountant, get you set up on our systems and meet your client success team. We'll set out timeframes, responsibilities, etc. to get the relationship going and help you get to a new level of success.</p></div>
  <div class="btn" style="left:545px;top:3300px;width:112px;height:35px">Book a call</div>
</section>

<!-- story -->
<section class="story">
  <div class="abs story-photo" role="img" aria-label="Photo of a hand writing on financial charts beside a calculator and laptop"></div>
  <svg class="abs" style="left:148px;top:3478px" width="420" height="430" viewBox="0 0 420 430"><polygon points="400,0 420,0 262,430 242,430" fill="#0E74BC"/><rect x="0" y="418" width="262" height="12" fill="#0E74BC"/></svg>
  <p style="top:3474px"><span class="hl">At Tovelbrook Accountants,</span> we know you are the kind of people who want to be successful and know that your business is being looked after. This gives you the time and stress-free mind to do the things you love doing and to see the people you love seeing.</p>
  <p style="top:3564px">To do that, you need to focus on the important issues in your business, know that the numbers are taken care of and your accountant is on your side. You also need to know that you are getting reliable feedback and advice that can be used to make decisions.</p>
  <p style="top:3654px">The problem is (and we hear it from a lot of people) that the current accountant only does numbers and nothing else, or they don't reply to you, or they don't offer any solutions, feels like they are on the other side of the table from you, or don't understand property or... Whatever the problem is, the end result is you are micromanaging and not getting the results or lifestyle you want.</p>
  <p style="top:3780px">We understand that we are your partners in your business and want to see you succeed. That's why we approach every problem as if its our own. So book a call today, so you can stop micromanaging and stressing and start focusing on the bigger picture and living life.</p>
  <div class="btn" style="left:598px;top:3872px;width:112px;height:35px">Book a call</div>
</section>

<!-- video band & footer -->
<div class="abs band-bg"></div>
<div class="abs video" role="img" aria-label="Video cover photo of a desk with calculator, watch and notes about income and investment"></div>
<svg class="abs play" width="40" height="40" viewBox="0 0 40 40"><circle cx="20" cy="20" r="18" fill="none" stroke="#222" stroke-width="2"/><path d="M16 12l12 8-12 8z" fill="#222"/></svg>
<div class="btn" style="left:545px;top:4175px;width:112px;height:35px">Book a call</div>

<footer class="footer">
  <div class="logo" style="left:148px;top:4398px;color:#fff;font-size:22px"><i style="background:#fff"></i><span>TOVELBROOK<br>ACCOUNTANTS</span></div>
  <h4 style="left:408px;top:4385px">Contact Us</h4>
  <div class="contact" style="top:4426px;font-size:13px;font-weight:500"><svg width="14" height="14" viewBox="0 0 36 36" fill="#fff"><path d="M8 4l6 1 2 7-4 3a20 20 0 009 9l3-4 7 2 1 6c-14 2-28-12-24-24z"/></svg>01632 960418</div>
  <div class="contact" style="top:4466px"><svg width="14" height="12" viewBox="0 0 14 12"><rect width="14" height="12" rx="1" fill="#fff"/><path d="M0 1l7 5 7-5" stroke="#0f8db0" fill="none"/></svg>info@tovelbrookaccountants.co.uk</div>
  <div class="contact" style="top:4496px"><svg width="12" height="16" viewBox="0 0 12 16"><path d="M6 0a6 6 0 00-6 6c0 4 6 10 6 10s6-6 6-10a6 6 0 00-6-6z" fill="#fff"/><circle cx="6" cy="6" r="2" fill="#0f8db0"/></svg>12 Harbour Lane, Eastwick,<br>EW4 2QT</div>
  <div class="social" style="left:411px"></div>
  <div class="social" style="left:453px;background:var(--teal);border:2px solid #fff"></div>
  <div class="social" style="left:495px"></div>
  <h4 style="left:655px;top:4385px">About Us</h4>
  <ul style="left:655px;top:4418px"><li>Meet The Team</li><li>Our Values</li><li>Software Solutions</li><li>Vacancies</li></ul>
  <h4 style="left:655px;top:4520px">Services</h4>
  <ul style="left:655px;top:4552px"><li>Company Services</li><li>Personal Services</li><li>Advisory Services</li></ul>
  <h4 style="left:820px;top:4385px">Who We Help</h4>
  <ul style="left:820px;top:4418px"><li>Property Investors and</li><li>Developers</li><li>Consultants</li><li>Medical Professionals</li><li>Buying or Selling a Business</li></ul>
  <div class="badge" style="left:820px;width:100px"></div>
  <div class="badge" style="left:936px;width:112px;background:rgba(255,255,255,.85)"></div>
  <div class="abs rule"></div>
  <p class="abs copy">© 2023 TOVELBROOK ACCOUNTANTS. Company No.: 10482736 &nbsp; | &nbsp; Privacy Policy &nbsp; | &nbsp; Cookies Policy &nbsp; | &nbsp; Terms of Business</p>
</footer>

</body>
</html>
```